Book Cover for Political Biography

Back round color, darker green.

This book is a political biography of Mr. Ter Haar Veldt who was a prominent politician in Curacao.

Looking for a modern toward the conservative look. The attached images can be used as place holders, we will get hi resolution ones to replace.

Book Title:
Mr. Dr. Anselm ter Haar Veldt: Pionier voor het Bestuurlijke Zelfbeschikking der Westelijke Eilanden

Name Author:
drs. K.J. (Thibault) Wessinghe MBA

Please leave space on the back for book description (one paragraph) and author biography (short paragraph)

```html
<!DOCTYPE html>
<html lang="nl">
<head>
<meta charset="utf-8">
<title>Pionier voor het Bestuurlijke Zelfbeschikking der Westelijke Eilanden</title>
<link rel="stylesheet" href="https://fonts.googleapis.com/css2?family=Cinzel:wght@600;700&family=Open+Sans:wght@700&display=swap">
<style>
  :root {
    --cover-green: #1a2a10;
    --frame-red: #c22a1e;
    --frame-glow: rgba(214, 60, 40, 0.55);
    --portrait-light: #c9c9c9;
    --portrait-mid: #8a8a8a;
    --portrait-dark: #3a3a3a;
    --text-white: #ffffff;
  }
  * { margin: 0; padding: 0; box-sizing: border-box; }
  html, body {
    width: 848px;
    height: 1200px;
    overflow: hidden;
    background: var(--cover-green);
  }
  .cover {
    position: relative;
    width: 848px;
    height: 1200px;
    background: var(--cover-green);
  }
  .portrait-frame {
    position: absolute;
    left: 172px;
    top: 40px;
    width: 481px;
    height: 688px;
    border: 5px solid var(--frame-red);
    box-shadow: 0 0 6px 2px var(--frame-glow);
  }
  .portrait {
    width: 100%;
    height: 100%;
    background:
      radial-gradient(ellipse 40% 35% at 50% 38%, var(--portrait-mid), transparent 70%),
      radial-gradient(ellipse 60% 40% at 50% 92%, var(--portrait-mid), transparent 75%),
      linear-gradient(160deg, var(--portrait-light) 0%, #a8a8a8 45%, var(--portrait-dark) 100%);
  }
  .book-title {
    position: absolute;
    left: 60px;
    right: 60px;
    top: 806px;
    text-align: center;
    font-family: "Cinzel", serif;
    font-weight: 700;
    color: var(--text-white);
    font-size: 29px;
    line-height: 38px;
    letter-spacing: 0.5px;
  }
  .book-title .title-main {
    display: block;
    font-size: 32px;
  }
  .book-title .title-sub {
    display: block;
    padding: 0 40px;
  }
  .author {
    position: absolute;
    left: 0;
    right: 0;
    top: 1122px;
    text-align: center;
    font-family: "Open Sans", sans-serif;
    font-weight: 700;
    font-size: 27px;
    color: var(--text-white);
  }
</style>
</head>
<body>
  <main class="cover">
    <div class="portrait-frame">
      <div class="portrait" role="img" aria-label="Zwart-wit portretfoto van Mr. Dr. Anselm ter Haar Veldt met bril en baard, in pak met das"></div>
    </div>
    <h1 class="book-title">
      <span class="title-main">Mr. Dr. Anselm ter Haar Veldt:</span>
      <span class="title-sub">Pionier voor het Bestuurlijke Zelfbeschikking der Westelijke Eilanden</span>
    </h1>
    <p class="author">drs. K.J. (Thibault) Wessinghe MBA</p>
  </main>
</body>
</html>
```